Launching a consulting business

I need a business card to launch a new consulting business. I provide executive level consultation throughout New York state to CEO and ED's who run and manage non-fo-profit corporations who support individuals with intellectual and developmental disabilities. The field is undergoing an evolution from a social model of care to more outcome based strategies. Having expertise in health care, leading a $50M business providing this service and working in the government creating policy I can bring to the Executive and corporations compassion, vision, strategy with a clear understanding of business practices for success. The field is moving to managed care. My background in health care management brings the expertise to create opportunities and possibilities. I currently have three projects I am consulting on - 1. Field expert assisting an accounting firm in the creation of a managed care application to become a managed care company supporting the ID/DD field. I crafted the care management model 2. Strategizing on product line creation to assure an agency is ready with a compendium services supporting the ID/DD field. 3. Facilitating a financial model to assist in predicting costs to render services in ID/DD. Developing and overlaying outcome measures to position agencies for effective marketing.
Quality is my passion and assuring all people live their life's dreams.
I would also like a template for letterhead stationary following what is created with my business card.
I wold like to incorporate a cranberry/sage tartan plaid within the design.

Please note my last name is spelled wrong on the attachment. I also do not want the tartan plaid used covering the entire card. i open to other ideas and suggestions.

Industry/Entity Type

Government

Contact Information for Business Card

Donna M Farris
Phone - 845-620-4178
Cell phone 845-733-2906
Email address - donnamfar@quillmail.com

```html
<!DOCTYPE html>
<html lang="en">
<head>
<meta charset="utf-8">
<title>Donna M Farris — Business Card</title>
<link rel="stylesheet" href="https://fonts.googleapis.com/css2?family=Arimo:wght@400&family=Merienda:wght@400&family=Raleway:wght@300&display=swap">
<style>
  :root {
    --backdrop: #e9e6e1;
    --card: #000000;
    --name-yellow: #f2e600;
    --title-cyan: #1e9ac4;
    --contact-white: #f2f2f2;
  }
  * { margin: 0; padding: 0; box-sizing: border-box; }
  html, body {
    width: 1200px;
    height: 848px;
    overflow: hidden;
    background: var(--backdrop);
  }
  .sheet {
    width: 1200px;
    height: 848px;
    display: flex;
    flex-direction: column;
    align-items: center;
    justify-content: center;
    gap: 48px;
  }
  .card {
    width: 630px;
    height: 360px;
    background: var(--card);
    position: relative;
    box-shadow: 0 6px 18px rgba(0, 0, 0, 0.25);
  }
  .card-front .name {
    position: absolute;
    top: 36px;
    left: 0;
    right: 0;
    text-align: center;
    font-family: "Arimo", Arial, sans-serif;
    font-size: 38px;
    color: var(--name-yellow);
    letter-spacing: -0.5px;
  }
  .card-front .title {
    position: absolute;
    top: 118px;
    left: 0;
    right: 0;
    text-align: center;
    font-family: "Merienda", cursive;
    font-size: 23px;
    line-height: 1.3;
    color: var(--title-cyan);
  }
  .card-front .contacts {
    position: absolute;
    top: 236px;
    left: 300px;
    list-style: none;
    font-family: "Arimo", Arial, sans-serif;
    font-size: 14px;
    line-height: 1.75;
    color: var(--contact-white);
  }
  .card-front .contacts li:nth-child(2) { padding-left: 14px; }
  .card-front .contacts li:nth-child(3) { padding-left: 14px; }
  .card-back {
    display: flex;
    align-items: center;
    justify-content: center;
  }
  .card-back .name-caps {
    font-family: "Raleway", sans-serif;
    font-weight: 300;
    font-size: 56px;
    text-transform: uppercase;
    letter-spacing: 2px;
    color: var(--name-yellow);
    text-shadow: 1px 1px 0 rgba(120, 110, 0, 0.8);
  }
</style>
</head>
<body>
  <main class="sheet">
    <section class="card card-front" aria-label="Business card front">
      <h1 class="name">Donna M Farris</h1>
      <p class="title">Executive<br>Business Strategy<br>Consultant</p>
      <ul class="contacts">
        <li>P - 845-620-4178</li>
        <li>M - 845-733-2906</li>
        <li>E - donnamfar@quillmail.com</li>
      </ul>
    </section>
    <section class="card card-back" aria-label="Business card back">
      <p class="name-caps">Donna M Farris</p>
    </section>
  </main>
</body>
</html>
```